Need 4 Page Brush Catalogue Redesign ASAP i will sellect any one.

I have attached my existing design please do the redesign with best look.

We are an industrial brush distributor in Texas. We provide high grade brushes to the rubber, metalwork, welding/pipeline, automotive, aerospace and other industries. So, if you are looking for one of the top-rated brass wire brushes suppliers, a wire wheel brush supplier, or any other kind of brush supplier in Texas, make us your choice!

Our brushes are manufactured using high quality raw materials and are appreciated for corrosion resistance, accurate dimensions, easy installation, smooth finish, long service life and sturdy design. The best part about our brushes is that they are stringently tested by our quality controller on different parameters.

Quarn Bristle has a reputation for flexibility, innovation and the ability to react to the needs of customers quickly. Having about 25 years of experience in this industry gives us an insight into the objectives and challenges of different projects and the ability of recommending the best solution for your application.

Get in touch with us today for finding out how we can help you with brush supplies for your business.
please check the link http://www.quarnbristle.example/

DON'T CALL
Updates

Please use attached logo at your design. Added Monday, June 12, 2017

Target Market(s)

brush industry reseller

Industry/Entity Type

Industrial

Font styles to use
Serif
Sans Serif

Colors

Designer to choose colors to be used in the design.

Requirements
Must have
• creative and i catchy
Nice to have
• must be creative
Should not have
• don't use clip art

```html
<!DOCTYPE html>
<html lang="en">
<head>
<meta charset="utf-8">
<title>Quarn Bristle Catalogue Cover</title>
<link rel="stylesheet" href="https://fonts.googleapis.com/css2?family=Fira+Sans:wght@800;900&family=Lato:wght@400;700&display=swap">
<style>
  :root {
    --navy: #173a66;
    --royal: #1d5190;
    --ink: #111418;
    --stage: #e6e6e6;
    --paper: #f4f4f4;
    --white: #ffffff;
  }
  html, body {
    margin: 0;
    width: 1200px;
    height: 1200px;
    overflow: hidden;
    background: var(--stage);
  }
  .spread { position: relative; width: 1200px; height: 1200px; }
  .page {
    position: absolute;
    width: 520px;
    height: 729px;
    overflow: hidden;
    background: var(--paper);
  }
  .page--back { left: 48px; top: 237px; }
  .page--front { left: 632px; top: 240px; width: 514px; height: 722px; }

  .back-photo {
    position: absolute; inset: 0;
    background:
      radial-gradient(ellipse 38% 30% at 62% 42%, rgba(255,255,255,0.75) 0%, rgba(255,255,255,0) 100%),
      radial-gradient(ellipse at 40% 45%, #e4e4e4 0%, #d2d2d2 60%, #c9c9c9 100%);
  }
  .back-brand {
    position: absolute; top: 38px; left: 0; right: 0;
    text-align: center;
    font-family: "Fira Sans", sans-serif;
    font-weight: 900;
    color: var(--navy);
  }
  .back-brand__name { font-size: 48px; line-height: 1; letter-spacing: -0.8px; }
  .back-brand__url { font-size: 20px; font-weight: 800; letter-spacing: 1.6px; margin-top: 10px; }
  .back-arc { position: absolute; left: 0; top: 0; width: 520px; height: 729px; }
  .back-address {
    position: absolute; left: 0; right: 0; top: 672px; margin: 0;
    text-align: center;
    font-family: "Lato", sans-serif; font-weight: 700;
    font-size: 8.5px; line-height: 1.25;
    color: var(--white);
  }

  .front-art { position: absolute; left: 0; top: 0; width: 514px; height: 722px; }
  .front-copy {
    position: absolute; left: 0; right: 0; top: 580px;
    text-align: center;
    font-family: "Lato", sans-serif;
  }
  .front-copy__kicker { font-size: 20px; font-weight: 400; color: var(--navy); margin: 0; line-height: 1.2; }
  .front-copy__title { font-size: 29px; font-weight: 400; color: var(--ink); margin: 2px 0 0; line-height: 1.2; }
  .front-brand {
    margin-top: 14px;
    font-family: "Fira Sans", sans-serif; font-weight: 900;
    color: var(--navy);
  }
  .front-brand__name { font-size: 26px; line-height: 1; letter-spacing: -0.4px; }
  .front-brand__url { font-size: 11px; font-weight: 800; letter-spacing: 1px; margin-top: 4px; }
</style>
</head>
<body>
<main class="spread">
  <section class="page page--back">
    <div class="back-photo" role="img" aria-label="Faint photo of a wire wheel brush"></div>
    <div class="back-brand">
      <div class="back-brand__name">QUARN BRISTLE</div>
      <div class="back-brand__url">WWW.QUARNBRISTLE.EXAMPLE</div>
    </div>
    <svg class="back-arc" viewBox="0 0 520 729">
      <defs>
        <linearGradient id="blueBand" x1="0" x2="1">
          <stop offset="0" stop-color="#173f70"/>
          <stop offset="0.5" stop-color="#1f5696"/>
          <stop offset="1" stop-color="#173f70"/>
        </linearGradient>
        <linearGradient id="mapTone" x1="0" y1="0" x2="0.6" y2="1">
          <stop offset="0" stop-color="#e8e8e6"/>
          <stop offset="0.6" stop-color="#dcdedb"/>
          <stop offset="0.85" stop-color="#cfe0c4"/>
          <stop offset="1" stop-color="#e2e4e0"/>
        </linearGradient>
      </defs>
      <path d="M0 418 Q260 170 520 418 V729 H0 Z" fill="#2a2a2a"/>
      <path d="M0 430 Q260 184 520 430 V729 H0 Z" fill="#ffffff"/>
      <path d="M0 438 Q260 194 520 438 V729 H0 Z" fill="url(#blueBand)"/>
      <circle cx="260" cy="497" r="96" fill="url(#mapTone)" role="img" aria-label="Street map showing the office location"/>
    </svg>
    <p class="back-address">Dana Quarn 1820 cedar hollow san antonio,<br>TX 78250 United States</p>
  </section>

  <section class="page page--front">
    <svg class="front-art" viewBox="0 0 514 722">
      <defs>
        <linearGradient id="frontPaper" x1="0" x2="1">
          <stop offset="0" stop-color="#e6e6e6"/>
          <stop offset="0.5" stop-color="#ffffff"/>
          <stop offset="1" stop-color="#e4e4e4"/>
        </linearGradient>
        <radialGradient id="wheelTone" gradientUnits="userSpaceOnUse" cx="332" cy="180" r="290">
          <stop offset="0" stop-color="#ffffff"/>
          <stop offset="0.24" stop-color="#fbfaf7"/>
          <stop offset="0.27" stop-color="#dcb880"/>
          <stop offset="0.36" stop-color="#c2944f"/>
          <stop offset="0.42" stop-color="#a77c44"/>
          <stop offset="0.45" stop-color="#34444f"/>
          <stop offset="0.7" stop-color="#18242c"/>
          <stop offset="1" stop-color="#0a1116"/>
        </radialGradient>
        <linearGradient id="paintTone" x1="1" y1="0" x2="0" y2="1">
          <stop offset="0" stop-color="#eef0ef"/>
          <stop offset="0.5" stop-color="#e3e6e5"/>
          <stop offset="0.72" stop-color="#c9b9a6"/>
          <stop offset="1" stop-color="#4a2a33"/>
        </linearGradient>
        <radialGradient id="wireTone" cx="0.55" cy="0.5" r="0.55">
          <stop offset="0" stop-color="#efe4c8"/>
          <stop offset="0.3" stop-color="#c9c0a4"/>
          <stop offset="0.45" stop-color="#8d866c"/>
          <stop offset="1" stop-color="#3c3a2e"/>
        </radialGradient>
      </defs>
      <rect width="514" height="722" fill="url(#frontPaper)"/>
      <circle cx="332" cy="196" r="290" fill="var(--navy)"/>
      <circle cx="332" cy="196" r="282" fill="#ffffff"/>
      <circle cx="332" cy="196" r="270" fill="url(#wheelTone)" role="img" aria-label="Photo of a black bristle wheel brush with brass hub"/>
      <circle cx="140" cy="432" r="116" fill="var(--navy)"/>
      <circle cx="140" cy="432" r="110" fill="url(#paintTone)" role="img" aria-label="Photo of a paint brush with wooden handle"/>
      <circle cx="310" cy="484" r="80" fill="var(--navy)"/>
      <circle cx="310" cy="484" r="74" fill="url(#wireTone)" role="img" aria-label="Photo of a steel wire wheel brush"/>
    </svg>
    <div class="front-copy">
      <p class="front-copy__kicker">TOP – RATED INDUSTRIAL BRUSH</p>
      <p class="front-copy__title">DISTRIBUTOR IN TEXAS</p>
      <div class="front-brand">
        <div class="front-brand__name">QUARN BRISTLE</div>
        <div class="front-brand__url">WWW.QUARNBRISTLE.EXAMPLE</div>
      </div>
    </div>
  </section>
</main>
</body>
</html>
```